"Made in Chicago" Baby Shower Invitation

I need a design for a baby shower invitation with the headline and theme of "Made in Chicago". The design should incorporate the colors/design of the Chicago flag. I have attached an image of the flag for your reference. The design should be sized 5-1/2 wide x 8-1/2 long. I want to be able to print two to a page on a standard 8-1/2 X 11" piece of (nice quality) paper on a standard home printer.
Copy:
Made in Chicago Baby Shower
For: Marla & Gordon
Date: Saturday, April 5, 2014
Time: 7:00 p.m.
Place: 27 West Halbrook Ave, 4B
RSVP by April 1 to Nadia Verholm/312-555-0193

Hello Designers - I corrected the size requirements of the invitation (bad math before) and added a few more notes of preference. Looking for a design that is more clean and graphic and less traditional, soft baby shower look. Thank you!

Friends & family of the 20-sometthing, urban professional couple who are having a baby.

Baby

Must have
• Chicago flag colors and/or image, the words "made in Chicago", and the (revised) size indicated.
Should not have
• Anything inappropriate or offensive to grandmother of said couple.

```html
<!DOCTYPE html>
<html lang="en">
<head>
<meta charset="utf-8">
<title>Made in Chicago Baby Shower Invitation</title>
<link rel="stylesheet" href="https://fonts.googleapis.com/css2?family=Federo&family=Yellowtail&family=Yanone+Kaffeesatz:wght@400&display=block">
<style>
  :root {
    --flag-red: #ee1c24;
    --frame-red: #d8312a;
    --flag-blue: #a9d9f1;
    --ink: #1c1c1c;
    --text-red: #d2343b;
    --paper: #ffffff;
    --tile-yellow: #f3c731;
    --tile-green: #5b9a2e;
    --tile-red: #c63a36;
  }
  html, body {
    margin: 0;
    padding: 0;
    overflow: hidden;
    background: #ffffff;
  }
  .invitation {
    position: relative;
    width: 754px;
    height: 1200px;
    box-sizing: border-box;
    border: 11px solid var(--frame-red);
    background: linear-gradient(to right, var(--flag-blue) 0, var(--flag-blue) 215px, var(--paper) 330px, var(--paper) 100%);
    overflow: hidden;
  }
  .star-column {
    position: absolute;
    left: 0;
    top: 0;
    width: 280px;
    height: 100%;
  }
  .details {
    position: absolute;
    left: 300px;
    right: 0;
    top: 0;
    bottom: 0;
    text-align: center;
    font-family: "Yanone Kaffeesatz", sans-serif;
    font-weight: 400;
    color: var(--ink);
  }
  .line {
    position: absolute;
    left: 0;
    right: 0;
    margin: 0;
    line-height: 1;
    white-space: nowrap;
    font-weight: 400;
  }
  .headline-made {
    top: 22px;
    left: 150px;
    font-family: "Yellowtail", cursive;
    font-size: 54px;
    color: var(--text-red);
    transform: rotate(-6deg);
    z-index: 2;
  }
  .headline-city {
    top: 56px;
    font-family: "Federo", sans-serif;
    font-size: 118px;
    color: var(--flag-blue);
    -webkit-text-stroke: 2px var(--ink);
    text-shadow: 0 0 8px rgba(0,0,0,0.55);
    letter-spacing: -2px;
  }
  .lead { font-size: 54px; }
  .accent { color: var(--text-red); }
  .come-help { top: 236px; }
  .parents { top: 298px; font-size: 66px; }
  .welcome { top: 362px; }
  .baby { top: 418px; font-size: 54px; }
  .baby-icons {
    position: absolute;
    top: 490px;
    left: 50%;
    transform: translateX(-50%);
  }
  .day { top: 638px; font-size: 60px; }
  .date { top: 700px; font-size: 72px; }
  .time { top: 770px; }
  .located { top: 836px; }
  .address { top: 888px; font-size: 50px; }
  .rsvp { top: 978px; font-size: 50px; }
  .host { top: 1044px; font-size: 50px; }
  .phone { top: 1104px; font-size: 50px; }
</style>
</head>
<body>
  <main class="invitation">
    <svg class="star-column" viewBox="0 0 280 1178" aria-hidden="true">
      <defs>
        <polygon id="flag-star" points="0,-100 19,-32.9 86.6,-50 38,0 86.6,50 19,32.9 0,100 -19,32.9 -86.6,50 -38,0 -86.6,-50 -19,-32.9"/>
      </defs>
      <use href="#flag-star" x="127" y="121" fill="var(--flag-red)"/>
      <use href="#flag-star" x="127" y="435" fill="var(--flag-red)"/>
      <use href="#flag-star" x="127" y="712" fill="var(--flag-red)"/>
      <use href="#flag-star" x="127" y="1032" fill="var(--flag-red)"/>
    </svg>

    <section class="details">
      <p class="line headline-made">Made in</p>
      <h1 class="line headline-city">Chicago</h1>

      <p class="line lead come-help">Come help</p>
      <p class="line accent parents">Marla &amp; Gordon</p>
      <p class="line lead welcome">Welcome their new</p>
      <p class="line accent baby">BABY!</p>

      <svg class="baby-icons" width="352" height="104" viewBox="0 0 352 104" role="img" aria-label="Three baby icon tiles: a teddy bear, a baby bottle and a pacifier">
        <rect x="4" y="8" width="100" height="92" rx="6" fill="var(--tile-yellow)"/>
        <circle cx="176" cy="52" r="50" fill="var(--tile-green)"/>
        <rect x="250" y="4" width="98" height="96" rx="10" fill="var(--tile-red)" transform="rotate(6 299 52)"/>
      </svg>

      <p class="line day">On Saturday,</p>
      <p class="line accent date">April 5, 2014</p>
      <p class="line lead time">7:00 p.m.</p>
      <p class="line lead located">Located at:</p>
      <p class="line accent address">27 West Halbrook Ave, 4B</p>
      <p class="line rsvp">RSVP by April 1st to</p>
      <p class="line host">Nadia Verholm @</p>
      <p class="line phone">312-555-0193</p>
    </section>
  </main>
</body>
</html>
```